NEW YORK Plumbing/utility company 10 year anniversary business card

Looking For simple back and front business card would like to include a few things in description
We offer 24/7 emergency service
residential
commercial
industrial
municipal
services offered
Plumbing
hydro excavation
hydro jetting
Well pumps
Sewer pumps
water mains
sewer mains

```html
<!DOCTYPE html>
<html lang="en">
<head>
<meta charset="utf-8">
<title>Riverline Water &amp; Sewer – Business Card</title>
<link href="https://fonts.googleapis.com/css2?family=Barlow:wght@500&family=Montserrat:wght@700;800&display=swap" rel="stylesheet">
<style>
  :root {
    --page-grey: #c3c3c3;
    --navy: #001a27;
    --brand-blue: #1767a8;
    --line-blue: #1c5d93;
    --alert-red: #e3242b;
    --white: #ffffff;
    --ink: #0a0a0a;
    --deep: #02101c;
  }
  * { margin: 0; padding: 0; box-sizing: border-box; }
  html, body {
    width: 1200px; height: 1200px; overflow: hidden;
    background: var(--page-grey);
  }
  .card {
    position: absolute; left: 349px; width: 502px; height: 324px; overflow: hidden;
  }
  .card-front { top: 233px; background: var(--navy); }
  .card-back  { top: 583px; }

  .line-art { position: absolute; inset: 0; }

  .texture-accent {
    position: absolute; left: 26px; top: 34px; width: 104px; height: 68px;
    background: radial-gradient(ellipse at center, rgba(28,93,147,0.35), rgba(28,93,147,0) 70%);
  }

  .brand {
    position: absolute; display: flex; align-items: center; gap: 8px;
    font-family: "Montserrat", sans-serif; font-weight: 800; color: var(--brand-blue);
    line-height: 1.05;
  }
  .brand-square { width: 26px; height: 26px; background: var(--brand-blue); flex: none; }
  .brand-name { font-size: 20px; letter-spacing: 0.04em; }
  .brand-name small { display: block; font-size: 10.5px; letter-spacing: 0.12em; margin-top: 3px; }
  .card-front .brand { left: 32px; top: 142px; }

  .person {
    position: absolute; right: 32px; top: 100px; text-align: right;
    font-family: "Barlow", sans-serif; font-weight: 500;
  }
  .person-name { color: var(--white); font-size: 26px; letter-spacing: 0.08em; line-height: 1; }
  .person-role { color: var(--alert-red); font-size: 18px; letter-spacing: 0.08em; margin-top: 7px; line-height: 1; }

  .contact {
    position: absolute; right: 31px; top: 202px; text-align: right;
    font-family: "Barlow", sans-serif; font-weight: 500; color: var(--white);
    font-size: 15.5px; letter-spacing: 0.08em;
  }
  .contact-row { display: flex; align-items: center; justify-content: flex-end; gap: 10px; height: 20px; }
  .contact-row svg { width: 16px; height: 14px; }

  .sector-bar {
    position: absolute; left: 0; top: 272px; width: 100%; height: 36px;
    border-top: 1.5px solid var(--white);
    display: flex; align-items: center; justify-content: center; gap: 12px;
    font-family: "Montserrat", sans-serif; font-weight: 800; color: var(--white);
    font-size: 12.5px; letter-spacing: 0.1em;
  }
  .sector-bar .dot { font-size: 10px; }
  .metal-strip {
    position: absolute; left: 0; bottom: 0; width: 100%; height: 16px;
    background: linear-gradient(90deg, #ffffff 0%, #b9d1e4 12%, #5f93c0 30%, #1565a6 44%, #7fa9cf 56%, #ffffff 71%, #9cbfdc 82%, #1565a6 100%);
  }

  .back-surface {
    position: absolute; inset: 0;
    background:
      radial-gradient(ellipse 120px 70px at 136px 160px, rgba(235,245,250,0.95), rgba(200,230,240,0.6) 55%, rgba(120,200,225,0) 100%),
      radial-gradient(ellipse 130px 120px at 405px 170px, rgba(225,235,240,0.95), rgba(190,210,220,0.75) 60%, rgba(140,180,200,0) 100%),
      radial-gradient(ellipse 280px 150px at 250px 160px, #3fb8d8, #1a78a8 50%, #0b3f6c 80%, var(--deep) 100%);
  }
  .card-back .brand { left: 62px; top: 143px; }

  .services {
    position: absolute; left: 312px; top: 78px;
    font-family: "Montserrat", sans-serif; color: var(--ink);
  }
  .services-title { font-weight: 800; font-size: 17px; letter-spacing: 0.08em; margin-left: 3px; }
  .services-list { list-style: none; margin-top: 4px; }
  .services-list li {
    display: flex; align-items: center; gap: 4px; height: 20.8px;
    font-weight: 800; font-size: 12.5px; letter-spacing: 0.01em;
  }
  .services-list svg { width: 12px; height: 12px; flex: none; }

  .emergency {
    position: absolute; left: 0; width: 100%; top: 276px; text-align: center;
    font-family: "Montserrat", sans-serif; font-weight: 800; color: var(--white);
    font-size: 18.5px; letter-spacing: 0.3em; padding-left: 8px;
  }
</style>
</head>
<body>

<section class="card card-front" aria-label="Business card front">
  <svg class="line-art" viewBox="0 0 502 324" aria-hidden="true">
    <polyline points="0,0 32,43.5" fill="none" stroke="var(--line-blue)" stroke-width="0.8"/>
    <line x1="130" y1="43.5" x2="502" y2="43.5" stroke="var(--line-blue)" stroke-width="0.8"/>
    <line x1="265" y1="165.5" x2="465" y2="165.5" stroke="var(--alert-red)" stroke-width="2"/>
  </svg>
  <div class="texture-accent" role="img" aria-label="Decorative hexagon line cluster"></div>

  <div class="brand">
    <span class="brand-square"></span>
    <span class="brand-name">RIVERLINE<small>WATER &amp; SEWER</small></span>
  </div>

  <div class="person">
    <p class="person-name">DANIEL REYES</p>
    <p class="person-role">OPS MANAGER</p>
  </div>

  <div class="contact">
    <p class="contact-row">845-555-0142
      <svg viewBox="0 0 24 24" aria-hidden="true"><path fill="var(--alert-red)" d="M6.6 10.8a15.5 15.5 0 0 0 6.6 6.6l2.2-2.2a1 1 0 0 1 1-.25 11.4 11.4 0 0 0 3.6.57 1 1 0 0 1 1 1V20a1 1 0 0 1-1 1A17 17 0 0 1 3 4a1 1 0 0 1 1-1h3.5a1 1 0 0 1 1 1c0 1.25.2 2.45.57 3.57a1 1 0 0 1-.25 1z"/></svg>
    </p>
    <p class="contact-row">hello@riverlineny.com
      <svg viewBox="0 0 24 18" aria-hidden="true"><rect x="0" y="0" width="24" height="18" fill="var(--alert-red)"/><polyline points="0,0 12,10 24,0" fill="none" stroke="var(--navy)" stroke-width="1.6"/><polyline points="0,18 9,8 M24,18 15,8" fill="none" stroke="var(--navy)" stroke-width="1.2"/></svg>
    </p>
  </div>

  <div class="sector-bar">
    <span>RESIDENTIAL</span><span class="dot">•</span>
    <span>COMMERCIAL</span><span class="dot">•</span>
    <span>MUNICIPAL</span><span class="dot">•</span>
    <span>INDUSTRIAL</span>
  </div>
  <div class="metal-strip"></div>
</section>

<section class="card card-back" aria-label="Business card back">
  <div class="back-surface" role="img" aria-label="Glowing blue hexagon mesh background"></div>
  <svg class="line-art" viewBox="0 0 502 324" aria-hidden="true">
    <polyline points="4,2 55,54 502,54" fill="none" stroke="#000" stroke-width="4" stroke-opacity="0.85"/>
    <polyline points="0,265.5 447,265.5 500,320" fill="none" stroke="#000" stroke-width="4" stroke-opacity="0.85"/>
  </svg>

  <div class="brand">
    <span class="brand-square"></span>
    <span class="brand-name">RIVERLINE<small>WATER &amp; SEWER</small></span>
  </div>

  <div class="services">
    <h2 class="services-title">OUR SERVICES</h2>
    <ul class="services-list">
      <li><svg viewBox="0 0 24 24" aria-hidden="true"><polygon fill="var(--alert-red)" points="12,1 15,9 23,9 16.5,14 19,22 12,17 5,22 7.5,14 1,9 9,9"/></svg>PLUMBING</li>
      <li><svg viewBox="0 0 24 24" aria-hidden="true"><polygon fill="var(--alert-red)" points="12,1 15,9 23,9 16.5,14 19,22 12,17 5,22 7.5,14 1,9 9,9"/></svg>HYDRO EXCAVATION</li>
      <li><svg viewBox="0 0 24 24" aria-hidden="true"><polygon fill="var(--alert-red)" points="12,1 15,9 23,9 16.5,14 19,22 12,17 5,22 7.5,14 1,9 9,9"/></svg>HYDRO JETTING</li>
      <li><svg viewBox="0 0 24 24" aria-hidden="true"><polygon fill="var(--alert-red)" points="12,1 15,9 23,9 16.5,14 19,22 12,17 5,22 7.5,14 1,9 9,9"/></svg>WELL PUMPS</li>
      <li><svg viewBox="0 0 24 24" aria-hidden="true"><polygon fill="var(--alert-red)" points="12,1 15,9 23,9 16.5,14 19,22 12,17 5,22 7.5,14 1,9 9,9"/></svg>SEWER PUMPS</li>
      <li><svg viewBox="0 0 24 24" aria-hidden="true"><polygon fill="var(--alert-red)" points="12,1 15,9 23,9 16.5,14 19,22 12,17 5,22 7.5,14 1,9 9,9"/></svg>WATER MAINS</li>
      <li><svg viewBox="0 0 24 24" aria-hidden="true"><polygon fill="var(--alert-red)" points="12,1 15,9 23,9 16.5,14 19,22 12,17 5,22 7.5,14 1,9 9,9"/></svg>SEWER MAINS</li>
    </ul>
  </div>

  <p class="emergency">24/7 EMERGENCY SERVICE</p>
</section>

</body>
</html>
```